Business Cards for IT Consulting Company (Managed Service Provider)

I am looking to have some business cards printed and would like some designs. We are an IT Consulting company based in Vancouver BC. I would like a nice clean and modern look to the cards. I have uploaded all the versions of my logo so parts can be used as needed. Here is a snippit from our website homepage:

Kelbrook Systems Ltd. is an IT Solutions Partner located in Vancouver BC, Canada. We offer IT solutions and support to customers in the greater Vancouver Area. With expertise in Microsoft platforms, as well as Linux and Mac OSX and over 12 years experience in the IT industry, Kelbrook Systems is dedicated to offering our clients top quality service and products. We take pride in the solutions we offer our customers. The greatest compliment a client can give us is to recommend our services.

Kelbrook Systems Ltd. offers a wide range of IT services from onsite service to remote support and managed service solutions. This allows clients to choose the support path that best suits their company’s needs. Supporting many different sized companies from small to enterprise level over the past 12 years Kelbrook Systems has the experience and expertise needed to ensure things run smoothly. Allowing our clients to focus on doing business.

Revolutionizing the way IT services are delivered.

Kelbrook Systems is dedicated to providing our clients with IT solutions that work and grow with them for years to come. This philosophy helps save money in the long run instead of replacing equipment constantly. Far too often IT solutions are not well thought out and while possibly solving the problem at hand, require replacement due to growth or quality within a very short time frame. Kelbrook Systems takes pride in providing solutions that will last and be able to accommodate growth without the need for replacement.

Industry/Entity Type

Information Technology

Contact Information for Business Card

Kelbrook Systems Ltd.
(Employee Name)
Eml: (Employees Email Address)
Web: kelbrook.me
Ph: 604-555-0142

Font styles to use
Serif
Sans Serif

Requirements
Must have
• The Company logo and company colors.
Nice to have
• - Our tag line: "Revolutionizing IT Services" or "Revolutionizing the way IT services are delivered."
• - Also I really like the idea of nature and technology together blending which is sort of where my logo came from so integrating that somehow onto the business cards would be great.

```html
<!DOCTYPE html>
<html lang="en">
<head>
<meta charset="utf-8">
<title>Kelbrook Systems Ltd. – Business Cards</title>
<link rel="stylesheet" href="https://fonts.googleapis.com/css2?family=Montserrat:wght@600&family=Questrial&display=swap">
<style>
  :root {
    --backdrop: #3b3b3d;
    --card: #ffffff;
    --brand-blue: #0fbfe9;
    --brand-blue-soft: #5fd3f0;
    --ink: #1f1f1f;
    --card-w: 540px;
    --card-h: 308px;
  }
  * { box-sizing: border-box; margin: 0; padding: 0; }
  html, body {
    width: 1200px;
    height: 688px;
    overflow: hidden;
    background: var(--backdrop);
  }
  .sheet {
    position: relative;
    width: 1200px;
    height: 688px;
    display: flex;
    align-items: center;
    justify-content: center;
    gap: 40px;
  }
  .card {
    position: relative;
    width: var(--card-w);
    height: var(--card-h);
    background: var(--card);
    overflow: hidden;
    box-shadow: 0 6px 18px rgba(0,0,0,0.35);
  }

  /* Front: company name and tagline */
  .card-front .brand {
    position: absolute;
    left: 58px;
    top: 112px;
    display: flex;
    align-items: center;
    gap: 14px;
  }
  .brand-square {
    width: 34px;
    height: 34px;
    border: 3px solid var(--brand-blue);
  }
  .brand-name {
    font-family: "Montserrat", sans-serif;
    font-weight: 600;
    font-size: 31px;
    letter-spacing: 0.5px;
    color: var(--brand-blue);
  }
  .tagline {
    position: absolute;
    left: 0;
    right: 0;
    bottom: 46px;
    text-align: center;
    font-family: "Questrial", sans-serif;
    font-size: 17px;
    letter-spacing: 0.6px;
    color: var(--ink);
  }

  /* Back: blue band and contact block */
  .band {
    position: absolute;
    inset: 0;
    width: 100%;
    height: 100%;
  }
  .contact {
    position: absolute;
    right: 26px;
    bottom: 26px;
    text-align: right;
    font-family: "Questrial", sans-serif;
    color: var(--ink);
    font-size: 16px;
    line-height: 21px;
  }
  .contact-name {
    font-family: "Montserrat", sans-serif;
    font-weight: 600;
    font-size: 18px;
    color: var(--brand-blue);
    letter-spacing: 0.8px;
  }
  .contact-role { margin-bottom: 4px; }
  .contact-line {
    display: flex;
    justify-content: flex-end;
    align-items: center;
    gap: 10px;
  }
  .contact-icon {
    width: 15px;
    height: 15px;
    flex: none;
  }
  .contact-role, .contact-name { padding-right: 0; }
</style>
</head>
<body>
<main class="sheet">

  <section class="card card-front" aria-label="Card front">
    <div class="brand">
      <span class="brand-square" aria-hidden="true"></span>
      <span class="brand-name">Kelbrook Systems Ltd.</span>
    </div>
    <p class="tagline">Revolutionizing the way IT services are delivered.</p>
  </section>

  <section class="card card-back" aria-label="Card back">
    <svg class="band" viewBox="0 0 540 308" preserveAspectRatio="none" aria-hidden="true">
      <defs>
        <linearGradient id="bandFade" x1="0" y1="0" x2="0" y2="1">
          <stop offset="0" stop-color="#0fbfe9"/>
          <stop offset="0.75" stop-color="#0fbfe9"/>
          <stop offset="1" stop-color="#5fd3f0"/>
        </linearGradient>
      </defs>
      <polygon points="0,72 82,0 350,0 150,308 0,308" fill="url(#bandFade)"/>
    </svg>

    <div class="contact">
      <p class="contact-name">Mark Dalton</p>
      <p class="contact-role">Network Engineer</p>
      <p class="contact-line">604-555-0142
        <svg class="contact-icon" viewBox="0 0 16 16" aria-label="Phone"><path d="M3 5c0-1.5 2-3 5-3s5 1.5 5 3l-2 1-1-2H6L5 6 3 5zM4 8h8l1 5H3l1-5z" fill="#0fbfe9"/></svg>
      </p>
      <p class="contact-line">mdalton@kelbrook.me
        <svg class="contact-icon" viewBox="0 0 16 16" aria-label="Email"><rect x="1" y="3.5" width="14" height="9" fill="#0fbfe9"/><path d="M1.5 4l6.5 5 6.5-5" fill="none" stroke="#fff" stroke-width="1.2"/></svg>
      </p>
      <p class="contact-line">www.kelbrook.me
        <svg class="contact-icon" viewBox="0 0 16 16" aria-label="Website"><circle cx="8" cy="8" r="6.5" fill="none" stroke="#0fbfe9" stroke-width="1.4"/><ellipse cx="8" cy="8" rx="3" ry="6.5" fill="none" stroke="#0fbfe9" stroke-width="1.1"/><path d="M1.5 8h13M2.5 5h11M2.5 11h11" stroke="#0fbfe9" stroke-width="1"/></svg>
      </p>
    </div>
  </section>

</main>
</body>
</html>
```